Design for Flavored drink product

I need a packaging design for flavoured drinks product.
The product is a flavoured drink product.

There will be various flavours i.e. orange, apple, strawberry, etc.
However, you may design the product using one sample flavour first (i.e. orange), as the designs of other flavours could be adjusted afterwards.

The temporary product name is: ZIBBLO

The measurement is 20,2 cm (Length) x 12,8 cm (Height).

The target customers are young audiences (10 years - 35 years old).

I want the product design to be something 'fun' and 'colourful'.
The design concept could be anything depends on your imagination.
Basically, I want you to be creative in designing the logo and the overall graphic design for the label.

I am hoping to have a product design that can stand out in the supermarket shelf.
It must be eye catchy and attractive.

- Create something different. Something extraordinary -

Note: You may refer to design sample attached

Thank you and Good Luck!

Thank you,
Marcus

```html
<!DOCTYPE html>
<html lang="en">
<head>
<meta charset="utf-8">
<title>ZIBBLO Orange – drink label</title>
<link href="https://fonts.googleapis.com/css2?family=Luckiest+Guy&family=Roboto+Condensed:ital,wght@0,800;1,700;1,800&display=swap" rel="stylesheet">
<style>
  :root {
    --page-bg: #f2f2f2;
    --label-silver-light: #ffffff;
    --label-silver-mid: #e9ebec;
    --label-silver-dark: #cfd3d6;
    --orange-deep: #e9560f;
    --orange-main: #f58a12;
    --orange-bright: #ffb21c;
    --orange-pale: #ffd66a;
    --white: #ffffff;
  }
  * { margin: 0; padding: 0; box-sizing: border-box; }
  html, body {
    width: 1200px; height: 1200px; overflow: hidden;
    background: var(--page-bg);
  }
  .canvas {
    position: relative; width: 1200px; height: 1200px;
    display: flex; align-items: center; justify-content: center;
  }
  .label {
    position: relative; width: 1100px; height: 697px; overflow: hidden;
    background: linear-gradient(90deg, var(--label-silver-dark) 0%, var(--label-silver-light) 18%, var(--label-silver-mid) 50%, var(--label-silver-light) 82%, var(--label-silver-dark) 100%);
    box-shadow: 0 6px 24px rgba(0,0,0,0.12);
  }
  .brand-name {
    position: absolute; left: 90px; top: 70px;
    font-family: "Luckiest Guy", sans-serif;
    font-weight: 400;
    font-size: 140px; line-height: 1; letter-spacing: 4px;
    color: var(--orange-main);
  }
  .feature-list {
    position: absolute; left: 100px; top: 250px; list-style: none;
  }
  .feature-list li {
    display: flex; align-items: center; gap: 12px;
    font-family: "Roboto Condensed", sans-serif; font-style: italic; font-weight: 800;
    font-size: 34px; line-height: 1.45; color: var(--orange-deep);
  }
  .feature-list svg { width: 26px; height: 26px; flex: none; }
  .citrus-art {
    position: absolute; right: -40px; top: 170px; width: 660px; height: 560px;
    border-radius: 48% 52% 0 0 / 55% 55% 0 0;
    background: radial-gradient(circle at 50% 45%, var(--orange-pale) 0%, var(--orange-bright) 45%, var(--orange-main) 80%);
  }
  .juice-wave {
    position: absolute; left: 0; bottom: 0; width: 100%; height: 200px;
  }
  .flavour-name {
    position: absolute; left: 580px; top: 440px;
    font-family: "Roboto Condensed", sans-serif; font-weight: 800; font-style: normal;
    font-size: 100px; line-height: 1; letter-spacing: 2px;
    color: var(--white);
  }
  .net-volume {
    position: absolute; right: 40px; bottom: 28px;
    font-family: "Roboto Condensed", sans-serif; font-weight: 700; font-style: italic;
    font-size: 26px; color: var(--white);
  }
</style>
</head>
<body>
  <main class="canvas">
    <section class="label">
      <div class="citrus-art" role="img" aria-label="Illustration of juicy orange slices with splashing juice and droplets"></div>
      <svg class="juice-wave" viewBox="0 0 1100 200" preserveAspectRatio="none" aria-hidden="true">
        <path d="M0 90 C200 40 380 140 600 90 C800 45 950 110 1100 70 L1100 200 L0 200 Z" fill="var(--orange-main)"/>
        <path d="M0 130 C220 90 420 170 640 125 C840 85 980 140 1100 115 L1100 200 L0 200 Z" fill="var(--orange-deep)"/>
      </svg>

      <h1 class="brand-name">ZIBBLO</h1>

      <ul class="feature-list">
        <li><svg viewBox="0 0 24 24"><path d="M3 13 L9 19 L21 5" fill="none" stroke="var(--orange-deep)" stroke-width="4" stroke-linecap="round" stroke-linejoin="round"/></svg>LOREM IPSUM</li>
        <li><svg viewBox="0 0 24 24"><path d="M3 13 L9 19 L21 5" fill="none" stroke="var(--orange-deep)" stroke-width="4" stroke-linecap="round" stroke-linejoin="round"/></svg>LOREM IPSUM</li>
        <li><svg viewBox="0 0 24 24"><path d="M3 13 L9 19 L21 5" fill="none" stroke="var(--orange-deep)" stroke-width="4" stroke-linecap="round" stroke-linejoin="round"/></svg>LOREM IPSUM</li>
        <li><svg viewBox="0 0 24 24"><path d="M3 13 L9 19 L21 5" fill="none" stroke="var(--orange-deep)" stroke-width="4" stroke-linecap="round" stroke-linejoin="round"/></svg>LOREM IPSUM</li>
      </ul>

      <p class="flavour-name">ORANGE</p>
      <p class="net-volume">Net Weight: 00 ml</p>
    </section>
  </main>
</body>
</html>
```